Need a landing page design updated

Need an existing landing page perfected, want it too look similar to one of Quince's landing pages in that it flows and is really aesthetically pleasing. The link to the landing page is below. I need this design updated asap. Please take the content directly from the page.

http://verdantrowfl-example.com/residential-services/

Target Market(s)

High end residential landscape customers on the gulf coast of Florida (Clearwater area)

Industry/Entity Type

Landscape Gardening

Font styles to use
Sans Serif
Decorative

Requirements
Must have
• I want to keep the written content the same on on the landing page, but would like to work on making both aesthetically appealing to the consumer. This is for high end residential clients on the gulf coast of florida, so think palm trees and sunny beaches with beautiful houses and gorgeous landscapes....look through www.verdantrowfl-example.com home page for an example of the houses we landscape.
Nice to have
• Would like it to flow as you scroll similar to Quince's landing pages.
• Look at how Quince's landing page flows, want similar here.....
• https://www.quince-example.com/lumaphone-z/
Should not have
• this landing page must be beautiful and must make a lot of sense as you scroll, am looking for a work of art....please do not submit generic templates or anything that can be easily done....I need real artistry.

```html
<!DOCTYPE html>
<html lang="en">
<head>
<meta charset="utf-8">
<title>Verdant Row — Residential Services</title>
<link href="https://fonts.googleapis.com/css2?family=Comfortaa:wght@300;400;700&display=swap" rel="stylesheet">
<style>
:root{
  --lime:#9ccc00;
  --lime-soft:#b5dc3c;
  --white:#ffffff;
  --ink:#2f2f2f;
  --muted:#6f6f6f;
  --grass-dark:#3d7a16;
  --grass-light:#8cc63f;
  --garden-deep:#1f2a15;
  --garden-mid:#34461f;
}
*{box-sizing:border-box;margin:0;padding:0}
html,body{width:1006px;height:1200px;overflow:hidden;background:var(--white)}
body{font-family:"Comfortaa",sans-serif;position:relative}
.grass-strip{position:absolute;left:0;top:0;width:1006px;height:38px;
  background:linear-gradient(180deg,#e8f3d6 0%,var(--grass-light) 45%,var(--grass-dark) 100%)}
.benefits{position:absolute;left:0;top:38px;width:1006px;height:395px;background:var(--lime);color:var(--white)}
.section-title{position:absolute;left:0;width:100%;text-align:center;font-weight:700;letter-spacing:.06em}
.benefits .section-title{top:87px;font-size:15px}
.rule{position:absolute;left:487px;width:32px;height:1px;background:var(--white)}
.benefits .rule{top:125px}
.benefit{position:absolute;top:164px;width:220px;text-align:center}
.benefit-icon{width:78px;height:70px;margin:0 auto;border-radius:6px;background:var(--lime-soft)}
.benefit p{margin-top:18px;font-size:13px;line-height:17px;letter-spacing:.05em;font-weight:300;white-space:nowrap}
.b1{left:152px}.b2{left:388px}.b3{left:628px}
.testimonials{position:absolute;left:0;top:433px;width:1006px;height:405px}
.testimonials .section-title{top:68px;font-size:15px;line-height:21px;color:var(--ink);letter-spacing:.08em}
.testimonials .rule{top:147px;background:var(--lime)}
.avatar{position:absolute;left:468px;top:182px;width:70px;height:70px;border-radius:50%;
  background:radial-gradient(circle at 50% 40%,#c9b3a0,#8a8f94)}
.quote{position:absolute;left:140px;top:271px;width:726px;text-align:center;font-size:13.5px;line-height:21px;
  font-style:italic;font-weight:300;color:var(--muted);letter-spacing:.04em;white-space:nowrap}
.author{position:absolute;left:0;top:325px;width:100%;text-align:center;font-size:10px;font-weight:700;color:var(--ink);letter-spacing:.08em}
.arrow{position:absolute;top:304px}
.arrow.prev{left:140px}.arrow.next{left:848px}
.flaws{position:absolute;left:0;top:838px;width:1006px;height:298px;color:var(--white);
  background:linear-gradient(180deg,#2b2e22 0%,var(--garden-mid) 45%,#3c4f1f 70%,var(--garden-deep) 100%)}
.flaws .section-title{top:64px;font-size:18px;line-height:25px;letter-spacing:.07em}
.flaws .rule{top:131px}
.flaw{position:absolute;left:168px;display:flex;align-items:center;font-size:14.5px;font-weight:300;letter-spacing:.06em}
.flaw .num{width:25px;height:25px;border:2px solid var(--lime);border-radius:50%;display:flex;align-items:center;justify-content:center;
  font-size:13px;font-weight:700;margin-right:25px}
.f1{top:167px}.f2{top:211px}
</style>
</head>
<body>
<div class="grass-strip" role="img" aria-label="Close-up of tall green grass blades"></div>

<section class="benefits">
  <h2 class="section-title">More benefits of having a well-maintained yard:</h2>
  <div class="rule"></div>
  <div class="benefit b1">
    <div class="benefit-icon" role="img" aria-label="Icon of a rising bar chart"></div>
    <p>In some cases, a<br>great-looking lawn can<br>increase your property's<br>value up to 20%.</p>
  </div>
  <div class="benefit b2">
    <div class="benefit-icon" role="img" aria-label="Icon of a house with a dollar sign"></div>
    <p>Your lawn and plants<br>reduce the energy<br>consumption – countering<br>the warming effects of<br>paved surfaces.</p>
  </div>
  <div class="benefit b3">
    <div class="benefit-icon" role="img" aria-label="Icon of an air filter with an arrow"></div>
    <p>They act as giant dust<br>filters, increasing air<br>quality, and removing<br>carbon dioxide from the<br>atmosphere.</p>
  </div>
</section>

<section class="testimonials">
  <h2 class="section-title">At Verdant Row, we do more than just keeping your landscape<br>in a pristine state. This is what some of our long-term clients say<br>about our approach:</h2>
  <div class="rule"></div>
  <div class="avatar" role="img" aria-label="Portrait photo of a smiling client"></div>
  <svg class="arrow prev" width="18" height="32" viewBox="0 0 18 32"><path d="M16 2 L2 16 L16 30" fill="none" stroke="var(--lime)" stroke-width="1.5"/></svg>
  <p class="quote">We are delighted with your landscaping, both with the design and implementation.It's not very<br>often these days that work exceeds expectations.</p>
  <p class="author">John Doe</p>
  <svg class="arrow next" width="18" height="32" viewBox="0 0 18 32"><path d="M2 2 L16 16 L2 30" fill="none" stroke="var(--lime)" stroke-width="1.5"/></svg>
</section>

<section class="flaws" role="img" aria-label="Darkened photo of a lush garden with lawn and flower beds">
  <h2 class="section-title">Do our services have flaws?<br>Yes. They have two giant ones.</h2>
  <div class="rule"></div>
  <div class="flaw f1"><span class="num">1</span>Your “new” garden will get all of your neighbors jealous.</div>
  <div class="flaw f2"><span class="num">2</span>Your friends will probably start inviting themselves over more frequently.</div>
</section>
</body>
</html>
```